Business Card Design for a Sound engineer and DJ

We would like a residn of the business card.

Logo must remain the same.
The card is for the owner of the company.
The business card is in Arabic as the company is based in Kuwait.
The company specializes in sound engineering for singers concerts and events and in addition DJ.
The color options is up to the designer but we would like it masculine as the owner is a man.

Target Market(s)

All ages

Industry/Entity Type

Media

Contact Information for Business Card

Name:
Eng. Faisal Barrak
م/فيصل براك

The name above is in Arabic and English.

Title: General Manager
Mobile: +965 96370482
Office: +965 22480637
Email: info@qamarwave.net

Address:
Office no. 3
1st floor
Marjan Complex
Hamad Faraj St.
Salmiya
Kuwait

Instagram: @qamarwave
Snap: qamarwave

Requirements
Nice to have
• can we have Instagram icon and snap icon and a phone vector and email?
• Instead of writing the words

```html
<!DOCTYPE html>
<html lang="en">
<head>
<meta charset="utf-8">
<title>Qamar Wave – Business Card</title>
<link rel="stylesheet" href="https://fonts.googleapis.com/css2?family=Open+Sans:wght@400;600;700&family=Cairo:wght@400;600&display=swap">
<style>
  :root{
    --page:#e9e7e4;
    --card-white:#ffffff;
    --blue-deep:#4f63c4;
    --blue-mid:#6f8fdc;
    --blue-light:#9fc6f0;
    --magenta:#a2238e;
    --violet:#7d4fb8;
    --ink:#3b3b45;
    --ink-soft:#5c5c66;
    --rule:#c9c9d2;
  }
  *{box-sizing:border-box;margin:0;padding:0}
  html,body{width:1200px;height:843px;overflow:hidden}
  body{background:var(--page);font-family:"Open Sans",Arial,sans-serif;position:relative}

  .card{position:absolute;left:290px;width:620px;height:354px;border-radius:4px;overflow:hidden;box-shadow:0 6px 18px rgba(0,0,0,.18)}
  .card--back{top:42px;background:radial-gradient(ellipse at 55% 45%,var(--blue-light) 0%,var(--blue-mid) 45%,var(--blue-deep) 100%)}
  .card--front{top:447px;background:var(--card-white)}

  /* back side */
  .back-brand{position:absolute;left:60px;top:118px;color:#fff;text-align:center;width:330px}
  .back-brand__name{font-family:"Open Sans",Arial,sans-serif;font-weight:600;font-size:40px;letter-spacing:6px;text-transform:uppercase}
  .back-brand__tag{font-size:13px;letter-spacing:2.5px;margin-top:4px;text-transform:uppercase}
  .back-brand__tag-ar{font-family:"Cairo",sans-serif;font-size:17px;margin-top:2px}
  .back-social{display:flex;justify-content:center;gap:12px;margin-top:10px}
  .back-social span{width:18px;height:18px;border:1.5px solid rgba(255,255,255,.8);border-radius:50%}
  .back-levels{position:absolute;right:40px;bottom:50px;width:150px;height:110px;opacity:.35;background:linear-gradient(to top,rgba(255,255,255,.7),rgba(255,255,255,0));border-radius:2px}

  /* front side */
  .brand{position:absolute;left:30px;top:120px;width:260px;text-align:center}
  .brand__row{display:flex;align-items:center;justify-content:center;gap:10px}
  .brand__square{width:26px;height:26px;background:var(--violet)}
  .brand__name{font-weight:600;font-size:30px;letter-spacing:4px;color:var(--violet);text-transform:uppercase}
  .brand__tag{font-size:11px;letter-spacing:2.2px;color:var(--violet);margin-top:8px;font-weight:600;text-transform:uppercase}
  .brand__tag-ar{font-family:"Cairo",sans-serif;font-size:15px;color:var(--violet);margin-top:0}

  .divider{position:absolute;left:305px;top:42px;width:1px;height:250px;background:var(--rule)}

  .contact{position:absolute;left:325px;top:40px;width:270px;color:var(--ink)}
  .contact__name{font-weight:700;font-size:23px;color:var(--magenta);line-height:1.1}
  .contact__name-ar{font-family:"Cairo",sans-serif;font-weight:600;font-size:17px;color:var(--magenta);line-height:1.3}
  .contact__title{font-weight:600;font-size:14px;color:var(--ink);margin-top:6px}
  .contact__address{font-size:13.5px;color:var(--ink-soft);line-height:1.35;margin-top:10px}
  .contact__lines{list-style:none;margin-top:10px}
  .contact__lines li{display:flex;align-items:center;gap:10px;font-size:13.5px;color:var(--ink-soft);line-height:1.55}
  .contact__lines svg{width:16px;height:16px;flex:none}

  .front-band{position:absolute;left:0;bottom:0;width:100%;height:48px;background:linear-gradient(to right,var(--blue-deep) 0%,var(--blue-mid) 35%,rgba(159,198,240,.6) 62%,rgba(255,255,255,0) 85%)}
  .front-levels{position:absolute;right:22px;bottom:14px;width:95px;height:62px;background:linear-gradient(to top,var(--blue-mid),var(--magenta));opacity:.55;border-radius:2px}
</style>
</head>
<body>

<section class="card card--back" aria-label="Card back">
  <div class="back-brand">
    <div class="back-brand__name">Qamar Wave</div>
    <div class="back-brand__tag">DJ - Sound Eng. - Lighting</div>
    <div class="back-brand__tag-ar" dir="rtl">دي جي - هندسة صوت - إضاءة</div>
    <div class="back-social"><span></span><span></span></div>
  </div>
  <div class="back-levels" role="img" aria-label="Faint sound level bars decoration"></div>
</section>

<section class="card card--front" aria-label="Card front">
  <div class="brand">
    <div class="brand__row">
      <span class="brand__square"></span>
      <span class="brand__name">Qamar Wave</span>
    </div>
    <div class="brand__tag">DJ - Sound Eng. - Lighting</div>
    <div class="brand__tag-ar" dir="rtl">دي جي - هندسة صوت - إضاءة</div>
  </div>

  <div class="divider"></div>

  <div class="contact">
    <div class="contact__name">Faisal Barrak</div>
    <div class="contact__name-ar" dir="rtl" style="text-align:left">م/فيصل براك</div>
    <div class="contact__title">General Manager</div>
    <div class="contact__address">
      Office no. 3, 1st floor<br>
      Marjan Complex<br>
      Hamad Faraj St.<br>
      Salmiya, Kuwait
    </div>
    <ul class="contact__lines">
      <li>
        <svg viewBox="0 0 16 16" aria-hidden="true"><rect x="4" y="1" width="8" height="14" rx="1.5" fill="none" stroke="var(--magenta)" stroke-width="1.6"/><line x1="7" y1="12.5" x2="9" y2="12.5" stroke="var(--magenta)" stroke-width="1.6"/></svg>
        +965 96370482
      </li>
      <li>
        <svg viewBox="0 0 16 16" aria-hidden="true"><path d="M4 1.5l2.5 3-1.5 1.8c.8 1.8 2 3 3.7 3.8L10.5 8.5l3 2.4-1.6 2.9C7 13.5 2.5 9 2.2 3.2z" fill="var(--magenta)"/></svg>
        +965 22480637
      </li>
      <li>
        <svg viewBox="0 0 16 16" aria-hidden="true"><rect x="1.5" y="3.5" width="13" height="9" fill="var(--magenta)"/><path d="M1.5 3.5L8 9l6.5-5.5" fill="none" stroke="#fff" stroke-width="1.3"/></svg>
        info@qamarwave.net
      </li>
    </ul>
  </div>

  <div class="front-band"></div>
  <div class="front-levels" role="img" aria-label="Small sound level bars decoration"></div>
</section>

</body>
</html>
```